Ayurveda & Wellness Website Redesign.

I need my website www.quilarest.com re-skinned. It is a wordpress site with Divi Builder.
I need a clearer funnel for new clients on the home page.
The funnel should provide questions for the potential client to answer. I can provide these, but I need a better funnel mechanism I think,
Possibly a video on the home page. Or an area of a video that I can change out.
So a better landing page is KEY!
The funnel should reroute to a video page and I should get informed when new clients enroll in the funnel.
Maybe I need a management system for this, but I need a recommendation.
Now I am using forms manager.
I need to be able to make changes using wordpress and/or Divi Builder.
The website should have a clean and spiritual feeling.
I can provide many more pictures and higher resolution.
I like the feeling of this website: http://tarnhollowherbals.com
Also this website: http://calmpetalroots.com/sessionswithorvena/
Target Market(s)
Women ages 25-65. People interested in health, yoga, spirituality.
Industry/Entity Type
Health And Wellness
Coding
Coded - Design and coding required
Requirements
Must have
- A clear sales funnel/enrollment mechanism on the home page. Could have a ebook download (I will provide) when they enroll.
Nice to have
- Currently using Slotra for clients to enroll in appointments. I would like to keep this.

```html
<!DOCTYPE html>
<html lang="en">
<head>
<meta charset="utf-8">
<title>Still Lotus – Ayurvedic Wellness</title>
<link href="https://fonts.googleapis.com/css2?family=Ubuntu:wght@400;500&family=Open+Sans:wght@400;600;700&display=swap" rel="stylesheet">
<style>
:root{
  --plum:#3a2a48;
  --gold:#c9a36a;
  --gold-soft:#d9b98a;
  --cream:#faf8f3;
  --card:#f3f1ea;
  --field:#ecebe7;
  --ink:#3b3340;
  --muted:#8a8290;
  --white:#ffffff;
  --lavender:#8c74bb;
  --lavender-soft:#c6b9de;
}
*{box-sizing:border-box;margin:0;padding:0}
html,body{width:1200px;height:1200px;overflow:hidden;background:var(--white)}
body{font-family:"Open Sans",sans-serif;color:var(--ink);position:relative}
.page{position:absolute;left:70px;top:1px;width:409px;height:1197px;background:var(--cream);box-shadow:0 0 6px rgba(0,0,0,.12);overflow:hidden}
h2{font-family:"Ubuntu",sans-serif;font-weight:400;color:var(--plum);text-align:center}
.rule{width:14px;height:1px;background:var(--gold);margin:3px auto}
.sub{font-size:5.4px;color:var(--gold);text-align:center;line-height:1.4}

/* nav */
.nav{height:23px;background:var(--plum);display:flex;align-items:center;justify-content:center;gap:7px;font-size:3.6px;color:#cfc6d8;letter-spacing:.2px;border-top:1px solid var(--gold)}
.nav .on{color:var(--white);font-weight:700}
.brand{font-family:"Ubuntu",sans-serif;font-size:11px;color:var(--gold-soft);margin:0 6px}

/* hero */
.hero{height:150px;position:relative;background:linear-gradient(100deg,#4a3a33 0%,#3d2e2f 40%,#5a4348 62%,#55613a 85%,#3f4d2c 100%);text-align:center;color:var(--white)}
.hero .play{position:absolute;left:189px;top:34px;width:30px;height:30px}
.hero h1{position:absolute;top:70px;width:100%;font-family:"Ubuntu",sans-serif;font-weight:500;font-size:10px;line-height:1.1;color:var(--gold-soft)}
.hero p{position:absolute;top:96px;width:100%;font-size:6px;line-height:1.35}

/* signup */
.signup{height:193px;position:relative;padding-top:29px}
.signup h2{font-size:10px}
.signup .art{position:absolute;left:0;top:112px;width:196px;height:68px;border-radius:0 40px 40px 0;background:linear-gradient(100deg,var(--lavender) 0%,#a28fca 45%,var(--lavender-soft) 80%,rgba(198,185,222,.35) 100%)}
.form{position:relative;z-index:1;width:240px;margin:11px auto 0}
.row{display:flex;gap:5px}
.field{flex:1;height:13px;background:var(--field);font-size:3.6px;color:var(--muted);padding:4px 5px}
.msg{height:41px;margin-top:10px;background:var(--field);font-size:3.6px;color:var(--muted);padding:6px}
.actions{display:flex;align-items:center;margin-top:8px;font-size:3.4px;color:var(--white)}
.btn{height:7px;padding:0 8px;display:flex;align-items:center;background:var(--plum)}
.btn.gold{background:var(--gold)}
.actions .gap{flex:1}
.refresh{width:5px;height:5px;border:1px solid var(--ink);border-radius:50%;margin-right:7px}

/* testimonials */
.testi{height:231px;padding-top:34px;background:#f6f4ee}
.testi h2{font-size:10px}
.cards{display:flex;justify-content:center;gap:6px;margin-top:20px}
.tcard{width:74px;height:119px;background:var(--card);position:relative;padding:22px 5px 0;font-size:3.3px;line-height:1.5;color:#4e4654;text-align:justify}
.avatar{position:absolute;left:22px;top:-12px;width:30px;height:30px;border-radius:50%;border:1.5px solid var(--gold);background:linear-gradient(#e8ddd3,#b89c88)}
.tcard p+p{margin-top:3px}
.tcard .name{position:absolute;bottom:7px;left:0;width:100%;text-align:center;color:var(--gold);font-size:3.4px}
.tcard .name::before{content:"";display:block;width:10px;height:1px;background:var(--gold);margin:0 auto 3px}

/* about */
.about{height:193px;position:relative;background:linear-gradient(90deg,#6a4e5a 0%,#4a3550 40%,#3a2a48 100%)}
.about .panel{position:absolute;left:89px;top:39px;width:234px;height:117px;background:var(--cream);padding:3px}
.about .inner{width:100%;height:100%;border:1px solid var(--gold);position:relative}
.about .figure{position:absolute;left:20px;top:10px;width:70px;height:95px;background:linear-gradient(#ece6dc,#d6ccc0)}
.about h2{position:absolute;left:95px;width:130px;top:26px;font-size:9.5px}
.about p{position:absolute;left:95px;width:130px;top:45px;font-size:5.5px;color:var(--gold);text-align:center;line-height:1.35}
.about .btn{position:absolute;left:134px;top:72px;font-size:3.4px;color:var(--white)}

/* blog */
.blog{height:231px;padding-top:26px}
.blog h2{font-size:10px}
.posts{display:flex;justify-content:center;gap:6px;margin-top:9px}
.post{width:76px;height:136px;background:var(--card);text-align:center}
.post .img{height:66px}
.post h3{font-size:3.6px;color:var(--plum);font-weight:600;margin-top:4px;line-height:1.3}
.post p{font-size:2.9px;line-height:1.45;color:#6a6270;padding:0 5px;margin-top:3px;height:22px}
.post .btn{display:inline-flex;margin-top:6px;font-size:2.8px;color:var(--white);height:6px;padding:0 5px}

/* newsletter */
.news{height:70px;background:linear-gradient(90deg,#c4a46a,#d4b67c 50%,#c9a06a);text-align:center;color:var(--white);padding-top:17px}
.news h2{color:var(--white);font-size:10px}
.news p{font-size:4px;margin-top:1px}
.subscribe{display:flex;justify-content:center;margin-top:8px}
.subscribe .in{width:82px;height:10px;background:var(--white);font-size:3.6px;color:var(--muted);text-align:left;padding:3px 4px}
.subscribe .btn{height:10px;font-size:3.8px;padding:0 7px;color:var(--white)}

/* footer */
.foot{height:92px;display:flex;gap:14px;padding:30px 0 0 90px;font-size:2.8px;line-height:1.55;color:#6a6270}
.foot h4{font-family:"Ubuntu",sans-serif;font-weight:400;font-size:5.5px;color:var(--plum);margin-bottom:4px}
.col-a{width:77px}
.col-b{width:55px}
.contact div{display:flex;gap:3px;align-items:center;margin-bottom:1px}
.contact i{width:3px;height:3px;background:var(--plum);border-radius:50%;display:inline-block}
.grid{display:grid;grid-template-columns:repeat(4,19px);grid-template-rows:repeat(2,19px);gap:1px}
.grid span{background:linear-gradient(135deg,#b08a4a,#5a3a22)}
.grid span:nth-child(odd){background:linear-gradient(135deg,#d9b06a,#7a5a2a)}
.bar{height:14px;background:var(--plum);display:flex;align-items:center;padding:0 90px;font-size:2.8px;color:#cfc6d8}
.bar .gap{flex:1}
.dots{display:flex;gap:3px}
.dots i{width:3.5px;height:3.5px;border-radius:50%;background:#cfc6d8;display:block}

/* annotation */
.note{position:absolute;left:478px;top:116px;width:292px}
.note h5{font-family:"Open Sans",sans-serif;font-weight:400;font-size:16px;color:#222;padding-left:18px;padding-bottom:4px;border-bottom:1px solid #333}
.note p{font-size:10px;color:#222;padding-left:22px;margin-top:4px}
</style>
</head>
<body>
<main class="page">
  <nav class="nav">
    <span class="on">HOME</span><span>CONSULTS</span><span>AYURVEDA</span>
    <span class="brand">Still Lotus</span>
    <span>WORKSHOPS</span><span>TESTIMONIALS</span><span>ABOUT MAREN</span>
  </nav>

  <section class="hero" role="img" aria-label="Wooden bowls of dried herbs, rose petals and flowers on a dark table">
    <svg class="play" viewBox="0 0 30 30"><circle cx="15" cy="15" r="13.5" fill="rgba(255,255,255,.12)" stroke="#fff" stroke-width="1.2"/><path d="M12 9 L21 15 L12 21Z" fill="#fff"/></svg>
    <h1>Ayurvedic Wellness Assessment<br>with Maren Holloway, PhDt</h1>
    <p>We believe the future of healthcare is in<br>prevention and Ayurveda is the key.</p>
  </section>

  <section class="signup">
    <div class="art" role="img" aria-label="Sprigs of lavender lying beside the form"></div>
    <h2>Sign Up Here</h2>
    <div class="rule"></div>
    <p class="sub">For a free Ayurvedic Wellness Assessment<br>with Maren Holloway, PhDt</p>
    <div class="form">
      <div class="row"><div class="field">Your Name</div><div class="field">Your Phone</div><div class="field">Your E-mail</div></div>
      <div class="msg">Message</div>
      <div class="actions">
        <span class="btn gold">Submit</span><span style="width:5px"></span><span class="btn">Reset</span>
        <span class="gap"></span><span class="refresh"></span>
        <span class="btn" style="margin-right:5px">Xk7 pQ2</span><span class="btn">Verification</span>
      </div>
    </div>
  </section>

  <section class="testi">
    <h2>Testimonials</h2>
    <div class="rule"></div>
    <p class="sub">For a free Ayurvedic Wellness Assessment<br>with Maren Holloway, PhDt</p>
    <div class="cards">
      <article class="tcard"><span class="avatar" role="img" aria-label="Client portrait"></span><p>"My experience with Maren as my Ayurvedic practitioner far exceeded my hopes. I came with low energy, poor sleep and a restless mind. She gave me clear, gentle routines and herbs that fit my days, and within a few weeks I felt lighter and calm again.</p><p>I applied her suggestions at home and my whole family felt the change. Thank you, Maren."</p><span class="name">Leila</span></article>
      <article class="tcard"><span class="avatar" role="img" aria-label="Client portrait"></span><p>Maren listened with patience and care, asking thoughtful questions about my habits, meals and rest. Her herbal plan and simple daily rituals changed how I eat, sleep and breathe.</p><p>Her sense of humour, warmth and insight made each visit a joy. The advice was practical and easy to follow, and I am still grateful for her kindness and wisdom."</p><span class="name">Marta</span></article>
      <article class="tcard"><span class="avatar" role="img" aria-label="Client portrait"></span><p>"Maren is a warm, wise and grounded guide. She blends deep study with practical advice that fits into a busy working life, and she always explains the reason behind each step.</p><p>All of these things make her an extraordinary healer. I recommend her to anyone seeking balance and support."</p><span class="name">Jonah</span></article>
    </div>
  </section>

  <section class="about" role="img" aria-label="Soft towels and flowers on a spa table">
    <div class="panel"><div class="inner">
      <div class="figure" role="img" aria-label="Woman seated in meditation"></div>
      <h2>About Maren</h2>
      <p>I am passionate about energy renewal and helping people resolve their health imbalances.</p>
      <span class="btn">Read more</span>
    </div></div>
  </section>

  <section class="blog">
    <h2>Our Blog</h2>
    <div class="rule"></div>
    <p class="sub">For a free Ayurvedic Wellness Assessment<br>with Maren Holloway, PhDt</p>
    <div class="posts">
      <article class="post"><div class="img" role="img" aria-label="Lavender with a wooden Ayurveda tag" style="background:linear-gradient(135deg,#6a3f8a,#c7b9a8)"></div><h3>Organic and Natural<br>Ingredients</h3><div class="rule"></div><p>Clean herbs and whole foods support balance for every dosha through the seasons.</p><span class="btn">Read more</span></article>
      <article class="post"><div class="img" role="img" aria-label="Carved wooden spice tokens" style="background:linear-gradient(135deg,#d8b48a,#a87a52)"></div><h3>Organic and Natural<br>Ingredients</h3><div class="rule"></div><p>Simple rituals to begin the day with warm water, oil and quiet breath, kept gently each morning.</p><span class="btn gold">Read more</span></article>
      <article class="post"><div class="img" role="img" aria-label="Jar of herbal paste on a table" style="background:linear-gradient(135deg,#3a1e12,#c07a2a)"></div><h3>High Quality Plant<br>Protein</h3><div class="rule"></div><p>Lentils, seeds and greens offer gentle plant protein for steady daily energy and calm digestion.</p><span class="btn">Read more</span></article>
    </div>
  </section>

  <section class="news" role="img" aria-label="Incense stick and rose petals on warm wood">
    <h2>Stay in touch with us</h2>
    <p>Lorem ipsum dolor sit amet, consectetur adipiscing elit, sed do eiusmod</p>
    <div class="subscribe"><span class="in">Enter your e-mail...</span><span class="btn">Subscribe</span></div>
  </section>

  <footer class="foot">
    <div class="col-a"><h4>About us</h4>Lorem ipsum dolor sit amet, consectetur adipiscing elit, sed do eiusmod tempor incididunt ut labore et dolore magna aliqua. Ut enim ad minim veniam, quis nostrud exercitation ullamco laboris nisi ut aliquip ex ea commodo consequat.</div>
    <div class="col-b contact"><h4>Contact us</h4><div><i></i>42 Cedar Lane, Riverton</div><div><i></i>hello@stilllotus.com</div><div><i></i>555 410 2298</div></div>
    <div><h4>Instagram</h4><div class="grid" role="img" aria-label="Grid of herb and spice photos"><span></span><span></span><span></span><span></span><span></span><span></span><span></span><span></span></div></div>
  </footer>
  <div class="bar"><span>2017 All Rights Reserved. Terms of use and Privacy Policy</span><span class="gap"></span><span class="dots"><i></i><i></i><i></i><i></i><i></i></span></div>
</main>

<aside class="note">
  <h5>Video Section</h5>
  <p>When user click here - video will appear fullwith screen</p>
</aside>
</body>
</html>
```